Brisket Dwelling Review is a leading provider of residential appraisal and home inspection products in S

I need a business card/logo designed that obviously describes my business. We are a residential appraisal and home inspection company in Springfield, MO. We offer residential appraisals, home inspection, pest inspection and radon gas measurement. We have been in business for 18 years and hold state certified residential appraisal licenses and VORMEL certified home inspection licenses. I have a logo that I really like and will attach, but would be open to new suggestions. I like more modern designs than traditional and would like a two sided card with our services, licenses and qualifications on the back.

```html
<!DOCTYPE html>
<html lang="en">
<head>
<meta charset="utf-8">
<title>Brisket Dwelling Review – Business Card</title>
<link rel="stylesheet" href="https://fonts.googleapis.com/css2?family=Open+Sans:wght@400;600;700;800&display=swap">
<style>
  :root {
    --bg: #ece7e1;
    --orange: #f39a2b;
    --orange-deep: #e9801a;
    --orange-light: #f8b24f;
    --black: #0c0c0c;
    --white: #ffffff;
    --brown: #7b5b3c;
    --gold: #c9a046;
    --ink: #1a1a1a;
  }
  * { box-sizing: border-box; margin: 0; padding: 0; }
  html, body { width: 1200px; height: 913px; overflow: hidden; }
  body {
    background: var(--bg);
    font-family: "Open Sans", Arial, sans-serif;
    position: relative;
  }
  .card {
    position: absolute;
    width: 540px;
    height: 310px;
    overflow: hidden;
    border-radius: 4px;
    box-shadow: 0 10px 28px rgba(0,0,0,.22);
  }
  .card-front { left: 80px; top: 110px; }
  .card-back { left: 580px; top: 490px; background: var(--white); }
  .card-art { position: absolute; inset: 0; }

  /* front */
  .cert-badge { position: absolute; left: 262px; top: 32px; }
  .brand-name {
    position: absolute;
    font-weight: 800;
    color: var(--brown);
    letter-spacing: -0.3px;
    line-height: 1.05;
  }
  .card-front .brand-name { left: 305px; top: 28px; font-size: 24px; color: var(--gold); width: 210px; }
  .address {
    position: absolute; right: 24px; top: 120px;
    color: var(--white); font-size: 14px; line-height: 1.35; text-align: right;
  }
  .holder { position: absolute; left: 28px; top: 176px; }
  .holder-name { font-size: 23px; font-weight: 700; color: var(--ink); letter-spacing: .5px; }
  .holder-role { font-size: 13px; color: var(--white); letter-spacing: .5px; margin-top: -2px; }
  .contact-list { list-style: none; margin-top: 6px; }
  .contact-list li {
    display: flex; align-items: center; gap: 8px;
    font-size: 14px; line-height: 18px; color: var(--ink); font-weight: 600;
  }
  .contact-list svg { width: 13px; height: 13px; fill: var(--white); stroke: var(--white); }

  /* back */
  .card-back .brand-name { left: 40px; top: 112px; font-size: 34px; width: 250px; }
  .brand-dot { display: inline-block; width: 12px; height: 12px; background: var(--orange); vertical-align: middle; margin-right: 8px; }
  .services {
    position: absolute; right: 20px; top: 34px;
    list-style: none; text-align: right;
  }
  .services li {
    font-size: 15px; font-weight: 600; color: var(--white);
    line-height: 19px; letter-spacing: .3px;
  }
  .services li::after {
    content: ""; display: inline-block; width: 9px; height: 9px;
    border-radius: 50%; background: var(--black); margin-left: 8px; vertical-align: 1px;
  }
  .tagline {
    position: absolute; left: 36px; bottom: 22px; width: 440px;
    font-size: 10.5px; font-weight: 700; color: var(--ink); line-height: 1.35;
  }
</style>
</head>
<body>

<section class="card card-front" aria-label="Business card front">
  <svg class="card-art" viewBox="0 0 540 310" aria-hidden="true">
    <defs>
      <linearGradient id="frontOrange" x1="0" y1="0" x2="1" y2="1">
        <stop offset="0" stop-color="#f8b24f"/>
        <stop offset="1" stop-color="#e9801a"/>
      </linearGradient>
    </defs>
    <rect width="540" height="310" fill="url(#frontOrange)"/>
    <polygon points="150,0 540,0 540,270" fill="#0c0c0c"/>
    <polygon points="128,0 142,0 540,276 540,286" fill="#0c0c0c"/>
    <line x1="146" y1="0" x2="540" y2="273" stroke="#c9a046" stroke-width="1.5"/>
  </svg>
  <svg class="cert-badge" width="30" height="30" viewBox="0 0 30 30" aria-label="Certification badge">
    <circle cx="15" cy="15" r="14" fill="#c9a046"/>
  </svg>
  <div class="brand-name">Brisket Dwelling Review</div>
  <address class="address">
    Brisket Dwelling Review 4417<br>
    W Larkspur Lane Suite C<br>
    Springfield, MO 65810
  </address>
  <div class="holder">
    <div class="holder-name">DORIAN VALE</div>
    <div class="holder-role">OWNER</div>
    <ul class="contact-list">
      <li><svg viewBox="0 0 24 24"><path d="M6.6 10.8a15 15 0 006.6 6.6l2.2-2.2c.3-.3.7-.4 1-.2 1.1.4 2.3.6 3.6.6.6 0 1 .4 1 1V20c0 .6-.4 1-1 1A17 17 0 013 4c0-.6.4-1 1-1h3.5c.6 0 1 .4 1 1 0 1.3.2 2.5.6 3.6.1.3 0 .7-.2 1z" stroke="none"/></svg>417-555-0142</li>
      <li><svg viewBox="0 0 24 24"><rect x="3" y="8" width="18" height="11" rx="2" stroke="none"/><rect x="7" y="3" width="10" height="6" stroke="none"/></svg>417-555-0187</li>
      <li><svg viewBox="0 0 24 24"><rect x="3" y="5" width="18" height="14" rx="1" fill="none" stroke-width="2"/><path d="M3 6l9 7 9-7" fill="none" stroke-width="2"/></svg>info@brisketdwelling.com</li>
      <li><svg viewBox="0 0 24 24"><circle cx="12" cy="12" r="9" fill="none" stroke-width="2"/><path d="M3 12h18M12 3c3 3 3 15 0 18M12 3c-3 3-3 15 0 18" fill="none" stroke-width="1.6"/></svg>www.brisketdwelling.com</li>
    </ul>
  </div>
</section>

<section class="card card-back" aria-label="Business card back">
  <svg class="card-art" viewBox="0 0 540 310" aria-hidden="true">
    <defs>
      <linearGradient id="backOrange" x1="0" y1="0" x2="1" y2="0">
        <stop offset="0" stop-color="#f39a2b"/>
        <stop offset="1" stop-color="#f8b24f"/>
      </linearGradient>
    </defs>
    <polygon points="250,0 540,0 540,310 300,310" fill="url(#backOrange)"/>
  </svg>
  <div class="brand-name"><span class="brand-dot"></span>Brisket Dwelling Review</div>
  <ul class="services">
    <li>APPRAISAL</li>
    <li>HOME INSPECTION</li>
    <li>TERMITE</li>
    <li>RADON</li>
    <li>WELL &amp; SEPTIC INSPECTION</li>
    <li>ENERGY AUDITS</li>
  </ul>
  <p class="tagline">With years of experience behind us, we're prepared to tackle anything from a first Time buyer's starter home or a seasoned buyer purchasing a luxurious dream home</p>
</section>

</body>
</html>
```